CTWI application splash screen

We need a 1024x768 image for use as an application splash screen.
The image will be displayed full screen on an 10 inch industrial PC 1024x768 screen while our application is launching. The image should convey that the application is "Waiting for connection to Wi-Fi access point..." and include a graphic of the industrial PC connected to the access point via an Ethernet cable. A list of troubleshooting steps should be included at the bottom of the image. The troubleshooting steps should not be the main focus of the image and should be shown in a smaller font (but still readable at 1024x768 displayed on a 10 inch screen).
I will include a mock up of the general idea of what we are looking for as well as image files for the industrial PC, a screenshot of our application to show on the PC's screen and the AP.
For general look and feel and a sense of corporate branding please review our website https://corvanetillageworks.com/. The splash screen should reflect corporate branding.
Target Market(s)
Users of our application
Industry/Entity Type
Agriculture

```html
<!DOCTYPE html>
<html lang="en">
<head>
<meta charset="utf-8">
<title>CTWI – Waiting for Wi-Fi access point</title>
<link href="https://fonts.googleapis.com/css2?family=Poppins:wght@400;500;600;700&display=swap" rel="stylesheet">
<style>
  :root {
    --brand-green: #43bd6b;
    --text-green: #3bb565;
    --white: #ffffff;
    --ink: #000000;
    --device-dark: #2b2b2b;
    --device-screen: #e6ece8;
    --ap-white: #f1f2f2;
  }
  * { box-sizing: border-box; margin: 0; padding: 0; }
  html, body {
    width: 1200px; height: 1200px; overflow: hidden;
    background: var(--ink);
    font-family: "Poppins", sans-serif;
  }
  .splash {
    position: absolute; left: 111px; top: 233px;
    width: 979px; height: 733px;
    background: var(--brand-green);
    overflow: hidden;
  }
  .status-card {
    position: absolute; left: 282px; top: 0;
    width: 413px; height: 163px;
    background: var(--white);
    border-radius: 0 0 26px 26px;
    display: flex; align-items: center; justify-content: center;
  }
  .status-title {
    color: var(--text-green);
    font-weight: 700; font-size: 34px; line-height: 34px;
    letter-spacing: 1.6px; text-align: center;
    padding-top: 6px;
  }
  .node {
    position: absolute; top: 215px;
    width: 241px; height: 241px; border-radius: 50%;
    background: var(--white);
  }
  .node--cab { left: 86px; }
  .node--ap { left: 651px; }
  .device-photo {
    position: absolute; left: 39px; top: 22px;
    width: 164px; height: 131px; border-radius: 8px;
    background: linear-gradient(180deg, #3a3a3a, #1f1f1f);
  }
  .device-photo::after {
    content: ""; position: absolute; left: 14px; top: 12px; right: 16px; bottom: 20px;
    background: linear-gradient(180deg, #f4f6f5 0%, var(--device-screen) 55%, #bfe6cb 100%);
    border-radius: 2px;
  }
  .ap-photo {
    position: absolute; left: 111px; top: 21px;
    width: 22px; height: 135px; border-radius: 4px;
    background: linear-gradient(90deg, #e2e4e4, var(--ap-white), #dcdede);
  }
  .node-label {
    position: absolute; left: 0; right: 0; text-align: center;
    color: var(--text-green);
  }
  .node-label__main {
    top: 164px; font-weight: 600; font-size: 17.5px; letter-spacing: 1.2px;
  }
  .node-label__sub {
    top: 187px; font-weight: 400; font-size: 13px; letter-spacing: 1px;
  }
  .node--ap .node-label__sub { font-size: 11px; top: 189px; }
  .link-lines { position: absolute; left: 0; top: 0; }
  .link-label {
    position: absolute; left: 0; right: 0; top: 479px;
    text-align: center; color: var(--white);
    font-weight: 600; font-size: 23px; letter-spacing: 1.6px;
  }
  .help-card {
    position: absolute; left: 276px; top: 579px;
    width: 426px; height: 160px;
    background: var(--white);
    border-radius: 24px 24px 0 0;
    padding: 10px 0 0 28px;
    color: var(--text-green);
  }
  .help-title {
    text-align: center; margin-left: -28px;
    font-weight: 600; font-size: 14.5px; letter-spacing: 1px;
    margin-bottom: 3px;
  }
  .help-list, .help-sublist { list-style: none; }
  .help-list li, .help-sublist li {
    font-size: 10.3px; line-height: 11.4px; position: relative; padding-left: 7px;
  }
  .help-list li::before, .help-sublist li::before {
    content: "•"; position: absolute; left: 0;
  }
  .help-sublist { margin-left: 12px; }
  .brand-mark {
    position: absolute; left: 855px; top: 615px;
    width: 90px; height: 90px; border-radius: 18px;
    background: var(--ink); border: 3px solid var(--white);
    display: flex; align-items: center; justify-content: center;
    color: var(--white); font-weight: 700; font-size: 24px; letter-spacing: 1px;
  }
</style>
</head>
<body>
  <main class="splash">
    <header class="status-card">
      <h1 class="status-title">Waiting for<br>connection to Wi-Fi<br>access point...</h1>
    </header>

    <section class="node node--cab">
      <div class="device-photo" role="img" aria-label="Industrial tractor cab computer showing the seeding application"></div>
      <div class="node-label node-label__main">TRACTOR CAB</div>
      <div class="node-label node-label__sub">COMPUTER</div>
    </section>

    <section class="node node--ap">
      <div class="ap-photo" role="img" aria-label="Outdoor Wi-Fi access point with two antennas"></div>
      <div class="node-label node-label__main">WI-FI ACCESS POINT</div>
      <div class="node-label node-label__sub">NETLYNK AP-220 OUTDOOR</div>
    </section>

    <svg class="link-lines" width="979" height="733" aria-hidden="true">
      <g stroke="#ffffff" stroke-width="4" stroke-linecap="round" stroke-dasharray="0 10.5" fill="none">
        <path d="M208 472 V518 H771 V472"/>
      </g>
    </svg>
    <div class="link-label">ETHERNET CABLE</div>

    <section class="help-card">
      <h2 class="help-title">TROUBLESHOOTING STEPS:</h2>
      <ul class="help-list">
        <li>This screen should only be visible for a short time on boot.</li>
        <li>If this screen stays visible for more than a minute:
          <ul class="help-sublist">
            <li>Verify that the Wi-Fi Access Point (AP) powers up when this system does (indicated by a green light on the side of the AP).</li>
            <li>Check the Ethernet cable between this system and the AP for damage, and replace it if necessary.</li>
            <li>Power-cycle this system and wait for it to reboot fully.</li>
            <li>If the issue persists, contact CTWI support for further assistance.</li>
          </ul>
        </li>
      </ul>
    </section>

    <div class="brand-mark">CTWI</div>
  </main>
</body>
</html>
```